Specialist aerospace company requires Powerpoint template

We are a company who delivers specialist engineering and testing services. We would like an updated Powerpoint template - specifically one that will be suitable to use in the production of training materials.
We would therefore like the following included:
-Our logo
-A copyright notice
-The course name (e.g. High Voltage Basics)
-The lesson name (e.g. Safe Clearances)
We wish to convey a professional image.

```html
<!DOCTYPE html>
<html lang="en">
<head>
<meta charset="utf-8">
<title>SkyVolt – Pitch Deck PowerPoint Template</title>
<link href="https://fonts.googleapis.com/css2?family=Poppins:wght@300;400;500;600;700&family=Raleway:wght@300;400&display=swap" rel="stylesheet">
<style>
:root{
  --slate:#4a525c;
  --slate-deep:#3f464f;
  --blue:#4b78a3;
  --blue-soft:#5a87b0;
  --white:#ffffff;
  --board-light:#ccd4d8;
  --board-dark:#454d57;
  --ink:#3d444d;
  --muted:#5e6670;
}
*{margin:0;padding:0;box-sizing:border-box}
html,body{width:1200px;height:2990px;overflow:hidden}
body{position:relative;background:linear-gradient(180deg,#c7d0d4 0%,#d6dde0 60%,#cfd7da 100%);font-family:'Poppins',sans-serif;color:var(--ink)}
.board-shape{position:absolute;left:0;top:0;width:1200px;height:1230px}
.slide{position:absolute;width:510px;height:286px;overflow:hidden;background:var(--white);box-shadow:0 6px 14px rgba(40,48,56,.18)}
.slide.dark{background:var(--slate)}
.slide svg.layer{position:absolute;left:0;top:0;width:510px;height:286px}
.abs{position:absolute}
.brand{color:var(--white);font-weight:500;font-size:19px;display:flex;align-items:center;gap:8px;letter-spacing:.2px}
.brand .mark{width:16px;height:16px;background:var(--white)}
.brand.small{font-size:10px;color:var(--slate);gap:4px}
.brand.small .mark{width:8px;height:8px;background:var(--blue)}
.title{color:var(--white);font-weight:600;font-size:19.5px;line-height:1.2}
.accent-bar{width:34px;height:3px;background:var(--blue-soft)}
.sub{color:var(--white);font-size:8.5px;line-height:1.55;font-weight:300}
.fine{color:var(--white);font-size:5.5px;font-weight:300}
.slide-heading{font-weight:600;font-size:17px;color:var(--slate);display:flex;align-items:center;gap:6px;left:0;top:22px}
.slide-heading .tab{width:25px;height:11px;background:var(--blue);color:var(--white);font-size:5px;line-height:11px;text-align:right;padding-right:6px}
.footer{position:absolute;left:0;bottom:6px;width:510px;height:14px}
.footer .band{position:absolute;left:0;top:0;width:400px;height:14px;background:var(--slate);clip-path:polygon(0 0,100% 0,98% 100%,0 100%);color:var(--white);font-size:5px;line-height:14px;padding-left:28px;font-weight:300}
.footer .brand{position:absolute;left:402px;top:0;height:14px}
.body-sm{font-size:7.8px;line-height:1.38;font-weight:300;color:var(--white)}
.body-xs{font-size:6.7px;line-height:1.36;font-weight:300}
.h-white{color:var(--white);font-weight:600;font-size:17px;line-height:1.15}
.card{background:var(--blue);color:var(--white);padding:11px 14px;font-size:8px;line-height:1.3;font-weight:300}
.card b{font-weight:600;display:block}
.agenda-row{position:absolute;height:28px;background:var(--slate);display:flex;align-items:center}
.agenda-row .num{width:40px;height:100%;background:var(--blue);color:var(--white);font-weight:600;font-size:11px;display:flex;align-items:center;justify-content:center}
.agenda-row .label{color:var(--white);font-size:11.5px;padding-left:10px}
.board-title{position:absolute;left:0;top:1062px;width:1200px;text-align:center;font-family:'Raleway',sans-serif;font-weight:300;font-size:29px;letter-spacing:3px;color:#4f5760}
.zoom{position:absolute;left:589px;top:1109px;width:22px;height:22px;border-radius:50%;background:var(--blue);color:var(--white);font-size:18px;line-height:21px;text-align:center;font-weight:300}
.zoom-note{position:absolute;left:0;top:1136px;width:1200px;text-align:center;font-size:11px;line-height:1.2;color:#5a626b;font-weight:300}
</style>
</head>
<body>

<svg class="board-shape" viewBox="0 0 1200 1230" aria-hidden="true">
  <polygon points="110,0 1200,0 1200,1220" fill="var(--board-dark)"/>
</svg>

<!-- Hero: title slide shown flat -->
<div class="slide dark" style="left:250px;top:230px;transform:scale(1.3725);transform-origin:0 0;box-shadow:0 10px 30px rgba(30,36,42,.35)">
  <svg class="layer" viewBox="0 0 510 286" preserveAspectRatio="none">
    <rect role="img" aria-label="Darkened photo of stacked motor stator laminations" width="510" height="286" fill="url(#hero-photo)"/>
    <defs><linearGradient id="hero-photo" x1="0" y1="0" x2="1" y2="1"><stop offset="0" stop-color="#4d555f"/><stop offset="1" stop-color="#454c56"/></linearGradient></defs>
    <polygon points="443,0 450,0 410,286 403,286" fill="var(--white)"/>
    <polygon points="455,0 510,0 510,286 415,286" fill="var(--blue)"/>
  </svg>
  <div class="abs brand" style="left:48px;top:50px"><span class="mark"></span>SkyVolt</div>
  <div class="abs title" style="left:47px;top:124px">Pitch Deck<br>Powerpoint Template</div>
  <div class="abs accent-bar" style="left:47px;top:178px"></div>
  <div class="abs sub" style="left:47px;top:188px">Subtitle Goes Here<br>June 2023</div>
  <div class="abs fine" style="left:47px;top:262px">www.skyvolt-test.com © SkyVolt 2022</div>
</div>

<div class="board-title">POWERPOINT TEMPLATE</div>
<div class="zoom">+</div>
<div class="zoom-note">click zoom<br>to see details</div>

<!-- Row 1 left: title -->
<div class="slide dark" style="left:76px;top:1357px">
  <svg class="layer" viewBox="0 0 510 286" preserveAspectRatio="none">
    <rect role="img" aria-label="Darkened photo of stacked motor stator laminations" width="510" height="286" fill="#4b535d"/>
    <polygon points="443,0 450,0 410,286 403,286" fill="var(--white)"/>
    <polygon points="455,0 510,0 510,286 415,286" fill="var(--blue)"/>
  </svg>
  <div class="abs brand" style="left:48px;top:50px"><span class="mark"></span>SkyVolt</div>
  <div class="abs title" style="left:47px;top:124px">Pitch Deck<br>Powerpoint Template</div>
  <div class="abs accent-bar" style="left:47px;top:178px"></div>
  <div class="abs sub" style="left:47px;top:188px">Subtitle Goes Here<br>June 2023</div>
  <div class="abs fine" style="left:47px;top:262px">www.skyvolt-test.com © SkyVolt 2022</div>
</div>

<!-- Row 1 right: agenda -->
<div class="slide" style="left:614px;top:1357px">
  <svg class="layer" viewBox="0 0 510 286" preserveAspectRatio="none">
    <polygon role="img" aria-label="Dark photo of copper wound stator coils" points="0,0 246,0 208,286 0,286" fill="#4a525c"/>
  </svg>
  <div class="abs h-white" style="left:32px;top:31px">Our<br>Agenda</div>
  <div class="abs accent-bar" style="left:32px;top:76px"></div>
  <div class="agenda-row" style="left:195px;top:43px;width:260px"><span class="num">01</span><span class="label">About Us</span></div>
  <div class="agenda-row" style="left:190px;top:80px;width:260px"><span class="num">02</span><span class="label">Services</span></div>
  <div class="agenda-row" style="left:186px;top:116px;width:260px"><span class="num">03</span><span class="label">Facilities</span></div>
  <div class="agenda-row" style="left:181px;top:153px;width:260px"><span class="num">04</span><span class="label">Application Areas</span></div>
  <div class="agenda-row" style="left:177px;top:190px;width:260px"><span class="num">05</span><span class="label">Insulation Evaluation</span></div>
  <div class="agenda-row" style="left:172px;top:226px;width:260px"><span class="num">06</span><span class="label">Contact Us</span></div>
</div>

<!-- Row 2 left: about us -->
<div class="slide" style="left:76px;top:1670px">
  <svg class="layer" viewBox="0 0 510 286" preserveAspectRatio="none">
    <rect x="0" y="62" width="510" height="163" fill="var(--blue)"/>
    <defs><linearGradient id="ice" x1="0" y1="0" x2="0" y2="1"><stop offset="0" stop-color="#9fc0dd"/><stop offset="1" stop-color="#5d87b3"/></linearGradient></defs>
    <polygon role="img" aria-label="Photo of an aircraft nose in an icing test chamber" points="254,26 481,26 463,247 223,247" fill="url(#ice)"/>
  </svg>
  <div class="abs slide-heading"><span class="tab">3</span>About Us</div>
  <div class="abs body-sm" style="left:28px;top:85px;width:190px">Drawing on over 25 years of experience in high voltage testing, we support companies developing the next generation of high voltage products for use in a range of applications including aerospace, automotive, rail and marine. With a well equipped laboratory facility we can evaluate the performance of insulation systems with a range of voltage types and in a range of environments.</div>
  <div class="footer"><div class="band">High Voltage Basics | Safe Clearances © SkyVolt 2022</div><div class="brand small"><span class="mark"></span>SkyVolt</div></div>
</div>

<!-- Row 2 right: text + cards -->
<div class="slide" style="left:614px;top:1670px">
  <div class="abs slide-heading"><span class="tab">3</span>Heading Goes Here</div>
  <div class="abs" style="left:30px;top:58px;width:440px;font-size:13.4px;line-height:1.3;color:var(--ink)">Lorem ipsum dolor sit amet, consectetur adipiscing elit, sed do eiusmod tempor incididunt ut labore et dolore magna aliqua. Ut enim ad minim veniam, quis nostrud exercitation ullamco laboris nisi ut aliquip ex ea commodo consequat.</div>
  <div class="abs card" style="left:30px;top:155px;width:179px;height:90px"><b>Title Goes Here</b>Lorem ipsum dolor sit amet, consectetur adipiscing elit, sed do eiusmod tempor incididunt ut labore et dolore magna aliqua.</div>
  <div class="abs card" style="left:269px;top:155px;width:211px;height:90px"><b>Title Goes Here</b>Lorem ipsum dolor sit amet, consectetur adipiscing elit, sed do eiusmod tempor incididunt ut labore et dolore magna aliqua.</div>
  <div class="footer"><div class="band">High Voltage Basics | Safe Clearances © SkyVolt 2022</div><div class="brand small"><span class="mark"></span>SkyVolt</div></div>
</div>

<!-- Row 3 left: section header -->
<div class="slide dark" style="left:76px;top:1979px">
  <div class="abs" style="left:44px;top:164px;width:20px;height:20px;background:var(--white)"></div>
  <div class="abs h-white" style="left:44px;top:206px;font-size:19px">Section Header</div>
</div>

<!-- Row 3 right: photo + text -->
<div class="slide" style="left:614px;top:1979px">
  <svg class="layer" viewBox="0 0 510 286" preserveAspectRatio="none">
    <defs><linearGradient id="lab" x1="0" y1="0" x2="1" y2="1"><stop offset="0" stop-color="#c9cbcd"/><stop offset=".6" stop-color="#6c6f73"/><stop offset="1" stop-color="#2e3135"/></linearGradient></defs>
    <polygon role="img" aria-label="Photo of an engineer wiring a test rig in the laboratory" points="0,0 241,0 204,286 0,286" fill="url(#lab)"/>
    <polygon points="214,176 483,176 475,258 204,258" fill="var(--blue)"/>
  </svg>
  <div class="abs" style="left:243px;top:30px;font-weight:600;font-size:17px;color:var(--slate)">Heading Goes Here</div>
  <div class="abs body-xs" style="left:245px;top:62px;width:232px;color:var(--ink);font-size:6.4px">SkyVolt was jointly founded in 2018 by Neil Harper (Technical Director) and Owen Marsh (Managing Director) in response to the growing needs of the aerospace sector as they develop higher voltage power dense electrical sectors. Our intention is to be more than a test house that delivers results with little understanding of their meaning – our test results are typically provided with a narrative that provides further discussion of the importance of the result and the proposed actions that the company should take in response to it. Our knowledge is informed by our work on a number of standards committees and the</div>
  <div class="abs body-sm" style="left:243px;top:192px;width:225px;font-size:8.6px;line-height:1.3">SkyVolt was jointly founded in 2018 by Neil Harper (Technical Director) and Owen Marsh (Managing Director) in response to the growing needs of the aerospace sector as they develop higher voltage</div>
</div>

<!-- Row 4 left -->
<div class="slide dark" style="left:76px;top:2289px">
  <svg class="layer" viewBox="0 0 510 286" preserveAspectRatio="none">
    <polygon points="262,0 266,0 230,286 226,286" fill="var(--blue)"/>
    <polygon role="img" aria-label="Photo of rows of stacked steel stator laminations" points="269,0 510,0 510,286 234,286" fill="#7b7f8a"/>
  </svg>
  <div class="abs h-white" style="left:40px;top:59px">Heading<br>Goes Here</div>
  <div class="abs accent-bar" style="left:40px;top:102px"></div>
  <div class="abs body-xs" style="left:40px;top:118px;width:164px;color:var(--white)">Lorem ipsum dolor sit amet, consectetur adipiscing elit, sed do eiusmod tempor incididunt ut labore et dolore magna aliqua. Ut enim ad minim veniam, quis nostrud exercitation ullamco laboris nisi ut aliquip ex ea commodo consequat. Duis aute irure dolor in reprehenderit in voluptate velit esse cillum dolore eu fugiat nulla pariatur. Excepteur sint occaecat cupidatat non proident, sunt in culpa qui officia deserunt mollit anim</div>
</div>

<!-- Row 4 right -->
<div class="slide dark" style="left:614px;top:2289px">
  <svg class="layer" viewBox="0 0 510 286" preserveAspectRatio="none">
    <polygon role="img" aria-label="Photo of copper wound stator coils" points="0,0 260,0 219,286 0,286" fill="#8a5a47"/>
    <polygon points="262,0 266,0 225,286 221,286" fill="var(--blue)"/>
  </svg>
  <div class="abs h-white" style="left:297px;top:59px">Heading<br>Goes Here</div>
  <div class="abs accent-bar" style="left:297px;top:102px"></div>
  <div class="abs body-xs" style="left:297px;top:118px;width:170px;color:var(--white)">Lorem ipsum dolor sit amet, consectetur adipiscing elit, sed do eiusmod tempor incididunt ut labore et dolore magna aliqua. Ut enim ad minim veniam, quis nostrud exercitation ullamco laboris nisi ut aliquip ex ea commodo consequat. Duis aute irure dolor in reprehenderit in voluptate velit esse cillum dolore eu fugiat nulla pariatur. Excepteur sint occaecat cupidatat non proident, sunt in culpa qui officia deserunt mollit anim</div>
</div>

<!-- Row 5 left: image grid -->
<div class="slide" style="left:76px;top:2601px">
  <div class="abs slide-heading"><span class="tab">3</span>Heading Goes Here</div>
  <svg class="layer" viewBox="0 0 510 286" preserveAspectRatio="none">
    <rect x="28" y="63" width="227" height="86" fill="var(--blue)"/>
    <rect role="img" aria-label="Photo of a hand holding a fibre optic connector" x="255" y="63" width="226" height="86" fill="#6f93b8"/>
    <rect role="img" aria-label="Photo of copper wound stator coils" x="28" y="149" width="227" height="96" fill="#8a5a47"/>
    <rect x="255" y="149" width="226" height="96" fill="var(--slate)"/>
  </svg>
  <div class="abs body-xs" style="left:38px;top:72px;width:205px;color:var(--white)">Lorem ipsum dolor sit amet, consectetur adipiscing elit, sed do eiusmod tempor incididunt ut labore et dolore magna aliqua. Sit amet dictum sit amet justo donec enim. Arcu risus quis varius quam quisque id diam vel quam. Elementum nibh tellus molestie nunc</div>
  <div class="abs body-xs" style="left:264px;top:185px;width:210px;color:var(--white)">Lorem ipsum dolor sit amet, consectetur adipiscing elit, sed do eiusmod tempor incididunt ut labore et dolore magna aliqua. Sit amet dictum sit amet justo donec enim. Arcu risus quis varius quam quisque id diam vel quam. Elementum nibh tellus molestie nunc</div>
  <div class="footer"><div class="band">High Voltage Basics | Safe Clearances © SkyVolt 2022</div><div class="brand small"><span class="mark"></span>SkyVolt</div></div>
</div>

<!-- Row 5 right: thank you -->
<div class="slide" style="left:614px;top:2601px;background:var(--blue)">
  <svg class="layer" viewBox="0 0 510 286" preserveAspectRatio="none">
    <polygon role="img" aria-label="Street map marking the company location" points="259,0 510,0 510,286 224,286" fill="#e9ecea"/>
  </svg>
  <div class="abs" style="left:34px;top:50px;font-weight:600;font-size:28px;color:var(--white)">Thank You</div>
  <div class="abs sub" style="left:34px;top:100px;font-size:8.4px;line-height:1.35">Unit 7, Kelvin House, 12 Ardent Way,<br>Northfield NF2 4QT</div>
  <div class="abs sub" style="left:34px;top:133px;font-size:8.4px;line-height:1.35">+44 (0)100 555 0142<br>info@skyvolt-test.com<br>www.skyvolt-test.com</div>
  <div class="abs brand" style="left:34px;top:212px;font-size:21px"><span class="mark"></span>SkyVolt</div>
</div>

</body>
</html>
```